New Business and Accounting Software need a Web Site

The website is for a Business and Accounting Software that has 8 products.
Each product has its owns logo and color, when you do the design have in consideration that we are looking the experience that when you change from one product page to another the look and feel adjust to the color and logo of the product.
The product are:
Ventas (Sales)
Compras (Purchases)
Contabilidad (Accounting)
Presupuesto (Budget)
Inventarios (Inventory)
Bancos (Banks)
NĂ³mina RH (Human Resources Payroll)
CRM (Customer Relationship Manager)

You can see how the main logo and variations are used in each page
- https://www.ufta.com/
- https://www.vemi.com/
- https://www.prulvin.com/

Our goal is to be similar to them.

I have created a word document to explain what I want.
You need to design:
1 Home Page
1 Product Landing Page
1 Product Detail Page
1 Price Page

I am attaching:
1. Main Logo
2. 8 Product Logos
3. Website Idea, you can create your own idea.

You are welcome to use other icons for the each product if you want.

Target Market(s)

Independet professionals and Small and Medium Companies

Industry/Entity Type

Business and Accounting Software

Coding

Coded - Design and coding required

Colors
0054AA
0677BA
7BADD7
CADEEF
E8F1F8

Requirements
Must have
• Must show all products in the main page

```html
<!DOCTYPE html>
<html lang="es">
<head>
<meta charset="utf-8">
<title>norvo.cr — Software de negocios y contabilidad</title>
<link rel="stylesheet" href="https://fonts.googleapis.com/css2?family=Lato:wght@400;700&family=Montserrat:wght@400;500;600&display=swap">
<style>
:root{
  --blue-900:#0054AA;
  --blue-700:#0677BA;
  --blue-400:#7BADD7;
  --blue-200:#CADEEF;
  --blue-100:#E8F1F8;
  --red:#D9432A;
  --ink:#1c1c1c;
  --text:#333;
  --grey-bg:#f4f4f4;
  --white:#fff;
  --head:'Montserrat',sans-serif;
  --body:'Lato',sans-serif;
}
*{box-sizing:border-box;margin:0;padding:0}
html,body{width:1200px;height:4501px;overflow:hidden;background:var(--white)}
body{position:relative;font-family:var(--body);color:var(--text)}
.abs{position:absolute}
.brand{display:flex;align-items:center;gap:10px;font-family:var(--head);font-weight:600;color:var(--blue-900)}
.brand .dot{border-radius:50%;background:var(--blue-900);flex:none}
.btn{display:inline-flex;align-items:center;justify-content:center;border-radius:22px;font-family:var(--body);font-size:13px;color:var(--white);text-decoration:none}
.btn-dark{background:var(--blue-900)}
.btn-light{background:var(--blue-400)}
.photo{position:absolute}

/* header */
.site-header{left:0;top:0;width:1200px;height:110px}
.site-header .brand{position:absolute;left:77px;top:30px;font-size:40px}
.site-header .brand .dot{width:58px;height:58px}
.main-nav{position:absolute;left:442px;top:48px;display:flex;gap:38px;font-size:13px;font-family:var(--head)}
.main-nav a{color:var(--ink);text-decoration:none}
.main-nav a.active{border-bottom:2px solid var(--blue-900);padding-bottom:6px}
.header-actions{position:absolute;left:847px;top:38px;display:flex;gap:13px}
.header-actions .btn{height:40px;width:134px}

/* hero */
.hero{left:0;top:110px;width:1200px;height:685px;overflow:hidden;background:#000}
.hero .photo{left:0;top:0;width:1200px;height:685px;background:linear-gradient(90deg,#000 0%,#000 28%,#5a5a5a 55%,#d9d9d9 78%,#eee 100%)}
.hero h1{position:absolute;left:75px;top:256px;font-family:var(--head);font-weight:500;font-size:31px;line-height:38px;color:var(--white)}
.hero .btn{position:absolute;left:77px;top:376px;width:134px;height:38px;background:var(--blue-900)}
.hero .slide-index{position:absolute;left:82px;top:585px;display:flex;align-items:center;gap:8px;font-size:11px;color:var(--blue-700)}
.hero .slide-index span.lines{display:flex;flex-direction:column;gap:7px}
.hero .slide-index span.lines i{display:block;height:2px;background:#aaa;width:30px}
.hero svg.swoosh{position:absolute;left:0;top:0}

/* product logos */
.products{left:0;top:900px;width:1200px;height:260px}
.product-logo{position:absolute;width:220px}
.product-logo .brand{font-size:36px;gap:8px}
.product-logo .brand .dot{width:62px;height:62px}
.product-logo small{position:absolute;left:72px;top:44px;font-family:var(--head);font-size:11px;letter-spacing:4px;color:#666}

.section-title{position:absolute;left:0;width:1200px;text-align:center;font-family:var(--head);font-size:30px;color:#444;font-weight:400}

/* profiles */
.profile{position:absolute;width:600px;height:493px;padding:72px 75px}
.profile h2{font-family:var(--head);font-weight:400;font-size:32px;color:var(--white)}
.profile hr{width:40px;border:0;border-top:2px solid rgba(255,255,255,.7);margin:30px 0 26px}
.profile p{font-size:13px;line-height:22px;color:var(--white);margin-bottom:20px}
.profile .btn{width:155px;height:38px;margin-top:16px}

/* plan cards */
.plan-card{position:absolute;top:2383px;width:250px;height:304px;padding:38px 26px;color:var(--white)}
.plan-card h3{font-family:var(--head);font-weight:400;font-size:30px}
.plan-card hr{width:32px;border:0;border-top:2px solid rgba(255,255,255,.7);margin:16px 0 14px}
.plan-card p{font-size:12.5px;line-height:22px}
.plan-card a{position:absolute;left:26px;top:262px;font-size:12.5px;color:var(--white)}

/* tabs */
.tab{position:absolute;top:2825px;height:51px;width:190px;display:flex;align-items:center;justify-content:center;font-family:var(--head);font-size:19px}
.tab-panel{left:0;top:2876px;width:1200px;height:566px;background:var(--grey-bg)}
.tab-panel h2{position:absolute;left:77px;top:63px;font-family:var(--head);font-weight:400;font-size:30px;color:var(--ink)}
.checklist{position:absolute;left:77px;top:120px;width:470px;list-style:none}
.checklist li{position:relative;padding-left:45px;font-size:13px;line-height:22px;margin-bottom:20px}
.checklist li svg{position:absolute;left:0;top:-2px}
.tab-panel .btn{position:absolute;left:75px;top:432px;width:155px;height:40px}
.tab-panel .photo{left:610px;top:59px;width:482px;height:437px;border-radius:70px 0 70px 0;background:linear-gradient(135deg,#e9eef3,#9fb7c9 50%,#41556a 85%,#c9a43c)}

/* feature cards */
.feature{position:absolute;top:3541px;width:250px;height:266px;padding:20px 34px;border-radius:0 34px 34px 34px;color:var(--white)}
.feature b{display:block;font-family:var(--head);font-weight:600;font-size:84px;line-height:90px}
.feature h3{font-family:var(--head);font-weight:400;font-size:23px;margin-top:4px;white-space:nowrap}
.feature p{font-size:12.5px;line-height:22px;margin-top:14px}
.feature.wide-title{padding-left:24px;padding-right:12px}
.feature.wide-title h3{font-size:17.5px;margin-top:10px}
.feature.wide-title p{margin-top:18px}

/* cta */
.cta{left:0;top:3912px;width:1200px;height:485px;background:var(--blue-900)}
.cta h2{position:absolute;left:114px;top:156px;font-family:var(--head);font-weight:500;font-size:34px;line-height:42px;color:var(--white)}
.cta .btn{position:absolute;left:111px;top:325px;width:170px;height:40px}
.cta-photo{left:601px;top:3852px;width:487px;height:489px;border-radius:140px 0 140px 0;background:linear-gradient(135deg,#dfe7f2,#6c8fc4 55%,#0e3f8a)}

/* footer */
.site-footer{left:0;top:4397px;width:1200px;height:104px}
.site-footer .brand{position:absolute;left:77px;top:28px;font-size:40px}
.site-footer .brand .dot{width:58px;height:58px}
.subscribe{position:absolute;left:384px;top:28px;display:flex;gap:21px}
.subscribe input{width:507px;height:46px;border:0;background:#f1f1f1;padding:0 20px;font-family:var(--body);font-size:13px;color:#333}
.subscribe button{width:213px;height:46px;border:0;background:var(--blue-900);color:var(--white);font-family:var(--body);font-size:13px}
</style>
</head>
<body>

<header class="site-header abs">
  <div class="brand"><span class="dot"></span>norvo.cr</div>
  <nav class="main-nav">
    <a class="active" href="#">Inico</a><a href="#">Soluciones</a><a href="#">Planes</a><a href="#">Contacto</a>
  </nav>
  <div class="header-actions">
    <a class="btn btn-dark" href="#">Get A Quote</a>
    <a class="btn btn-light" href="#">Free Trial</a>
  </div>
</header>

<section class="hero abs">
  <div class="photo" role="img" aria-label="Persona trabajando en un escritorio con monitores que muestran hojas de cálculo"></div>
  <svg class="swoosh" width="1200" height="685" viewBox="0 0 1200 685">
    <path d="M430 668 C700 640 950 610 1200 590 L1200 628 C950 642 700 660 430 685 Z" fill="#0054AA"/>
    <path d="M800 650 C950 628 1080 612 1200 605 L1200 622 C1080 630 950 642 805 660 Z" fill="#7BADD7"/>
    <path d="M0 685 L0 680 C150 680 300 676 430 668 L430 685 Z" fill="#fff"/>
    <path d="M430 685 C700 660 950 642 1200 628 L1200 685 Z" fill="#fff"/>
  </svg>
  <h1>Take More Control<br>of Your Business</h1>
  <a class="btn" href="#">Free Trial</a>
  <div class="slide-index">02 <span class="lines"><i></i><i></i><i></i></span></div>
</section>

<section class="products abs" aria-label="Productos">
  <div class="product-logo" style="left:77px;top:28px"><div class="brand"><span class="dot" style="background:#E8A03A"></span>norvo.cr</div><small>VENTAS</small></div>
  <div class="product-logo" style="left:367px;top:32px"><div class="brand"><span class="dot" style="background:#7BADD7"></span>norvo.cr</div><small>COMPRAS</small></div>
  <div class="product-logo" style="left:646px;top:30px"><div class="brand"><span class="dot" style="background:#C34A8C"></span>norvo.cr</div><small style="letter-spacing:1px">CONTABILIDAD</small></div>
  <div class="product-logo" style="left:926px;top:32px"><div class="brand"><span class="dot" style="background:#C8323A"></span>norvo.cr</div><small style="letter-spacing:1px">INVENTARIOS</small></div>
  <div class="product-logo" style="left:77px;top:152px"><div class="brand"><span class="dot" style="background:#555"></span>norvo.cr</div><small>BANCOS</small></div>
  <div class="product-logo" style="left:365px;top:150px"><div class="brand"><span class="dot" style="background:#2AAE8C"></span>norvo.cr</div><small style="letter-spacing:1px">PRESUPUESTO</small></div>
  <div class="product-logo" style="left:650px;top:152px"><div class="brand"><span class="dot" style="background:#D0395B"></span>norvo.cr</div><small style="letter-spacing:1px">INVENTARIOS</small></div>
  <div class="product-logo" style="left:924px;top:150px"><div class="brand"><span class="dot" style="background:#6B6FD1"></span>norvo.cr</div><small>CRM</small></div>
</section>

<h2 class="section-title" style="top:1196px">¿Cuál es tu perfil?</h2>

<section class="profile" style="left:0;top:1293px;background:var(--blue-900)">
  <h2>Profesional</h2><hr>
  <p>Lorem Ipsum is simply dummy text of the printing and typesetting industry has been the industry's standard dummy text ever since the 1500s,</p>
  <p>when an unknown printer took a galley of type and scrambled it to make a type specimen book. It has survived not only five centuries, but also the leap into electronic typesetting, remaining essentially unchanged. It was popularised in the 1960s</p>
  <a class="btn btn-light" href="#">Mas informacion</a>
</section>
<div class="photo" style="left:600px;top:1293px;width:600px;height:493px;background:linear-gradient(135deg,#eae6e1,#cbc3b8 55%,#8d8479)" role="img" aria-label="Profesional trabajando con documentos y una laptop"></div>

<div class="photo" style="left:0;top:1786px;width:600px;height:492px;background:linear-gradient(135deg,#c9c9c9,#f2f2f2 45%,#7f95b3 80%,#2d3f5f)" role="img" aria-label="Contador revisando gráficos con calculadora"></div>
<section class="profile" style="left:600px;top:1786px;background:var(--blue-400);padding-left:66px">
  <h2>Contador</h2><hr>
  <p>Lorem Ipsum is simply dummy text of the printing and typesetting industry has been the industry's standard dummy text ever since the 1500s,</p>
  <p>when an unknown printer took a galley of type and scrambled it to make a type specimen book. It has survived not only five centuries, but also the leap into electronic typesetting, remaining essentially unchanged. It was popularised in the 1960s</p>
  <a class="btn btn-dark" href="#">Mas informacion</a>
</section>

<article class="plan-card" style="left:77px;background:var(--blue-400)">
  <h3>Micro</h3><hr>
  <p>Lorem Ipsum is simply dummy text of the printing and typesetting industry has been the industry's standard dummy text ever since the 1500s,</p>
  <a href="#">Mas informacion</a>
</article>
<article class="plan-card" style="left:349px;background:var(--blue-900)">
  <h3>Micro</h3><hr>
  <p>Lorem Ipsum is simply dummy text of the printing and typesetting industry has been the industry's standard dummy text ever since the 1500s,</p>
  <a href="#">Mas informacion</a>
</article>
<article class="plan-card" style="left:625px;background:var(--red)">
  <h3>Empresarial</h3><hr>
  <p>Lorem Ipsum is simply dummy text of the printing and typesetting industry has been the industry's standard dummy text ever since the 1500s,</p>
  <a href="#">Mas informacion</a>
</article>
<div class="photo" style="left:875px;top:2383px;width:252px;height:304px;background:linear-gradient(160deg,#8a8580,#4e4a46 60%,#2f2c2a)" role="img" aria-label="Equipo de trabajo reunido en una mesa vista desde arriba"></div>

<div class="tab" style="left:197px;background:#f4f4f4;color:var(--ink)">Tab 1</div>
<div class="tab" style="left:404px;background:var(--blue-400);color:var(--white)">Tab 2</div>
<div class="tab" style="left:606px;background:var(--blue-900);color:var(--white)">Tab 3</div>
<div class="tab" style="left:811px;background:var(--red);color:var(--white)">Tab 4</div>

<section class="tab-panel abs">
  <h2>Title</h2>
  <ul class="checklist">
    <li><svg width="28" height="28" viewBox="0 0 28 28"><circle cx="13" cy="15" r="11" fill="none" stroke="#0054AA" stroke-width="2.4"/><path d="M8 14l5 5 12-13" fill="none" stroke="#0054AA" stroke-width="3" stroke-linecap="round" stroke-linejoin="round"/></svg>Lorem Ipsum is simply dummy text of the printing and typesetting industry has been the industry's.</li>
    <li><svg width="28" height="28" viewBox="0 0 28 28"><circle cx="13" cy="15" r="11" fill="none" stroke="#0054AA" stroke-width="2.4"/><path d="M8 14l5 5 12-13" fill="none" stroke="#0054AA" stroke-width="3" stroke-linecap="round" stroke-linejoin="round"/></svg>Lorem Ipsum is simply dummy text of the printing and typesetting industry has been the industry's standard dummy text ever since the 1500s,</li>
    <li><svg width="28" height="28" viewBox="0 0 28 28"><circle cx="13" cy="15" r="11" fill="none" stroke="#0054AA" stroke-width="2.4"/><path d="M8 14l5 5 12-13" fill="none" stroke="#0054AA" stroke-width="3" stroke-linecap="round" stroke-linejoin="round"/></svg>Lorem Ipsum is simply dummy text of the printing and typesetting industry has been the industry's standard dummy text ever since the 1500s,</li>
    <li><svg width="28" height="28" viewBox="0 0 28 28"><circle cx="13" cy="15" r="11" fill="none" stroke="#0054AA" stroke-width="2.4"/><path d="M8 14l5 5 12-13" fill="none" stroke="#0054AA" stroke-width="3" stroke-linecap="round" stroke-linejoin="round"/></svg>Lorem Ipsum is simply dummy text of the printing and typesetting industry has been the industry's.</li>
  </ul>
  <a class="btn btn-dark" href="#">Mas informacion</a>
  <div class="photo" role="img" aria-label="Manos escribiendo en una laptop con un panel de gráficos en pantalla"></div>
</section>

<article class="feature" style="left:77px;background:var(--blue-400);border-radius:0 0 0 40px">
  <b>1.</b><h3>Paga por uso</h3>
  <p>Lorem Ipsum is simply dummy text of the printing and typesetting.</p>
</article>
<article class="feature" style="left:344px;background:var(--blue-900)">
  <b>2.</b><h3>Sin Contrato</h3>
  <p>Lorem Ipsum is simply dummy text of the printing and typesetting.</p>
</article>
<article class="feature" style="left:610px;background:var(--red)">
  <b>3.</b><h3>En La Nube</h3>
  <p>Lorem Ipsum is simply dummy text of the printing and typesetting.</p>
</article>
<article class="feature wide-title" style="left:875px;background:#000">
  <b>4.</b><h3>Multiples Dispositivos</h3>
  <p>Lorem Ipsum is simply dummy text of the printing and typesetting.</p>
</article>

<section class="cta abs">
  <h2>?Que Esperas Para Crear<br>Una Cuenta Gratis En<br>Norvo.Cr?</h2>
  <a class="btn btn-light" href="#">Crear Cuenta Gratis</a>
</section>
<div class="photo cta-photo" role="img" aria-label="Mano usando una calculadora sobre gráficos financieros"></div>

<footer class="site-footer abs">
  <div class="brand"><span class="dot"></span>norvo.cr</div>
  <form class="subscribe">
    <input type="text" value="Reciba Las actualizaciones de Norvo" aria-label="Correo">
    <button type="button">Suscribirme</button>
  </form>
</footer>

</body>
</html>
```